Brand new letterhead, business card, email signature etc.

We are a financial company in London, UK. Our website is www.quorvane.com. We're wanting a complete remodel of the company colours, letter head, business cards, email signatures, etc. Looking to keep the same font for the company name. I have upload a colour palette that we want to work with. We're looking for company letterhead for outgoing letters/ correspondence, letterhead for internal documentation, email signatures, e-letters. etc. Ultimately we will redesign the entire website also. It is important that our clients get a strong, secure, warm, trustworthy, solid feeling and first impression.
Updates

Designs look the same

Target Market(s)

Institutional investors, (ultra) high net worth individuals

Industry/Entity Type

Finance, Invesments banking.

Font styles to use
Other font styles liked:
• Current font is "Champagne & Limousines"

Requirements
Must have
• Must use the colours provided on the PDF uploaded to the portal. The purple = main colour. The red = accent colour.
Nice to have
• Nice to use same font as now for the company name "Marlowin". Font is "Champagne & Limousines". Nice to have some reference to the old logo flower, but only subtle.
Should not have
• Do not use the colour red from our website. Use the colours provided on the colour palette PDF that I uploaded in the portal.

```html
<!DOCTYPE html>
<html lang="en">
<head>
<meta charset="utf-8">
<title>Marlowin Letterhead</title>
<link rel="stylesheet" href="https://fonts.googleapis.com/css2?family=Josefin+Sans:wght@300&family=Open+Sans:wght@400;600;700&display=swap">
<style>
  :root {
    --accent-red: #d05547;
    --brand-plum: #47343c;
    --paper: #e9e9e9;
    --backdrop: #d6d3d0;
    --body-grey: #8a8a8a;
    --contact-grey: #5a5257;
    --rule: #c9c5bb;
  }
  * { box-sizing: border-box; margin: 0; padding: 0; }
  html, body { width: 1200px; height: 1200px; overflow: hidden; }
  body { background: var(--backdrop); position: relative; font-family: "Open Sans", sans-serif; }

  .letterhead {
    position: absolute; left: 160px; top: 30px;
    width: 880px; height: 1140px;
    background: var(--paper);
    box-shadow: 0 2px 10px rgba(0,0,0,.15);
    overflow: hidden;
  }
  .top-band { position: absolute; left: 0; top: 0; width: 100%; height: 34px; background: var(--accent-red); }
  .contact-strip { position: absolute; left: 779px; top: 0; width: 44px; height: 234px; background: var(--brand-plum); }

  .brand { position: absolute; left: 114px; top: 98px; display: flex; align-items: center; gap: 15px; }
  .brand-square { width: 57px; height: 57px; border: 1px solid var(--brand-plum); }
  .brand-name {
    font-family: "Josefin Sans", sans-serif; font-weight: 300;
    font-size: 31px; letter-spacing: 7px; color: var(--brand-plum);
    line-height: 1; padding-top: 4px;
  }

  .contact-row {
    position: absolute; left: 578px; width: 201px;
    text-align: right; padding-right: 11px;
    font-family: "Josefin Sans", sans-serif; font-weight: 300;
    font-size: 12px; line-height: 16px; color: var(--contact-grey);
  }
  .contact-row.phone { top: 94px; }
  .contact-row.web { top: 148px; }
  .contact-row.address { top: 201px; }
  .contact-rule { position: absolute; left: 578px; width: 201px; height: 1px; background: var(--rule); }
  .contact-rule.first { top: 141px; }
  .contact-rule.second { top: 189px; }
  .contact-icon { position: absolute; left: 791px; width: 20px; height: 20px; }
  .contact-icon.phone { top: 101px; }
  .contact-icon.web { top: 155px; }
  .contact-icon.pin { top: 208px; }

  .recipient { position: absolute; left: 112px; top: 284px; color: var(--body-grey); font-size: 13px; line-height: 18.5px; }
  .recipient-name { color: var(--brand-plum); font-weight: 700; font-size: 19px; line-height: 24px; margin-bottom: 8px; }

  .letter-body { position: absolute; left: 112px; top: 428px; width: 656px; color: var(--body-grey); font-size: 12.4px; line-height: 18.45px; }
  .letter-body p { text-align: justify; margin-bottom: 18.4px; }

  .sign-off { position: absolute; right: 85px; top: 900px; text-align: right; }
  .signature-mark { display: inline-block; width: 135px; height: 30px; background: linear-gradient(90deg, rgba(71,52,60,.10), rgba(71,52,60,.22)); border-radius: 3px; }
  .signer-name { color: var(--brand-plum); font-weight: 600; font-size: 16.5px; margin-top: 6px; line-height: 22px; }
  .signer-role { color: var(--body-grey); font-size: 13px; line-height: 18px; }
</style>
</head>
<body>
  <main class="letterhead">
    <div class="top-band"></div>
    <div class="contact-strip"></div>

    <div class="brand">
      <div class="brand-square"></div>
      <div class="brand-name">MARLOWIN</div>
    </div>

    <div class="contact-row phone">+000 12345 6789<br>+000 12345 6789</div>
    <div class="contact-rule first"></div>
    <div class="contact-row web">urwebsitename.com<br>urname@email.com</div>
    <div class="contact-rule second"></div>
    <div class="contact-row address">1234 Street name, town/city,<br>state/country, post/zip 012345.</div>

    <svg class="contact-icon phone" viewBox="0 0 20 20" aria-hidden="true">
      <path d="M3 8 Q10 3 17 8 L15 10 L13 8.5 L13 7 Q10 6 7 7 L7 8.5 L5 10 Z" fill="#fff"/>
      <rect x="5" y="10" width="10" height="6" rx="1" fill="#fff"/>
    </svg>
    <svg class="contact-icon web" viewBox="0 0 20 20" aria-hidden="true" fill="none" stroke="#fff" stroke-width="1.3">
      <circle cx="10" cy="10" r="7.5"/>
      <path d="M3 8 Q10 11 17 7 M5 15 Q9 9 14 3 M8 17 Q12 12 17 12"/>
    </svg>
    <svg class="contact-icon pin" viewBox="0 0 20 20" aria-hidden="true">
      <path d="M10 2 C6.5 2 4.5 4.5 4.5 7.5 C4.5 11.5 10 18 10 18 C10 18 15.5 11.5 15.5 7.5 C15.5 4.5 13.5 2 10 2 Z" fill="#fff"/>
      <circle cx="10" cy="7.5" r="2" fill="var(--brand-plum)"/>
    </svg>

    <section class="recipient">
      <div class="recipient-name">Name Surname</div>
      Senior Executive<br>
      Address goes here. Street, City, Country<br>
      contact@yourmail.com<br>
      000-987-654-321
    </section>

    <section class="letter-body">
      <p>Lorem ipsum dolor sit amet, consectetur adipisicing elit, sed do eiusmod tempor incididunt ut labore et dolore magna aliqua. Ut enim ad minim veniam, quis nostrud exercitation ullamco laboris nisi ut aliquip ex ea commodo consequat. Duis aute irure dolor in reprehenderit in voluptate velit esse cillum dolore eu fugiat nulla pariatur. Excepteur sint occaecat cupidatat non proident, sunt in culpa qui officia deserunt mollit anim id est laborum. Sed ut perspiciatis unde omnis iste natus error sit voluptatem accusantium doloremque laudantium, totam rem aperiam, eaque ipsa quae ab illo inventore veritatis et quasi architecto beatae vitae dicta sunt explicabo. Nemo enim ipsam voluptatem quia voluptas sit aspernatur aut odit aut fugit, sed quia consequuntur magni dolores eos qui ratione voluptatem sequi nesciunt. Neque porro voluptatem sequi nesciunt. Nemo enim ipsam voluptatem quia voluptas.</p>
      <p>Lorem ipsum dolor sit amet, consectetur adipisicing elit, sed do eiusmod tempor incididunt ut labore et dolore magna aliqua. Ut enim ad minim veniam, quis nostrud exercitation ullamco laboris nisi ut aliquip ex ea commodo consequat. Duis aute irure dolor in reprehenderit in voluptate velit esse cillum dolore eu fugiat nulla pariatur. Excepteur sint occaecat cupidatat non proident, sunt in culpa qui officia deserunt mollit anim id est laborum. Sed ut perspiciatis unde omnis iste natus error sit voluptatem accusantium doloremque laudantium, totam rem aperiam, eaque ipsa quae ab illo inventore veritatis et quasi architecto beatae vitae dicta sunt explicabo. Nemo enim ipsam voluptatem quia voluptas sit aspernatur aut odit aut.</p>
      <p>Lorem ipsum dolor sit amet, consectetur adipisicing elit, sed do eiusmod tempor incididunt ut labore et dolore magna aliqua. Ut enim ad minim veniam, quis nostrud exercitation ullamco laboris nisi ut aliquip ex ea commodo consequat. .</p>
    </section>

    <section class="sign-off">
      <div class="signature-mark" role="img" aria-label="Handwritten signature"></div>
      <div class="signer-name">NAME SURNAME</div>
      <div class="signer-role">General Manager</div>
    </section>
  </main>
</body>
</html>
```